Design a compelling Tarnwell Business Card that will drive people to my site

I want a business card that I can give to people—less to tell them who I am and more to direct them to my website. My website is a portal for Crestlane Aquatics Officials and a place for people who want to become Crestlane Aquatics Officials.
I am uploading my official company logo as well as a business card mockup that I did on my own. Please feel free to completely stray from this design.
I've included a screen recording of the homepage of my website as well.
Target Market(s)
Crestlane Aquatics Officials and people who desire to become one
Contact Information for Business Card
website url
Look and feel
Each slider illustrates characteristics of the customer's brand and the style your logo design should communicate.

```html
<!DOCTYPE html>
<html lang="en">
<head>
<meta charset="utf-8">
<title>Tarnwell Business Card</title>
<link rel="stylesheet" href="https://fonts.googleapis.com/css2?family=Poppins:wght@400;600;700&display=swap">
<style>
  :root {
    --navy: #2b4285;
    --brand-blue: #2f4a9e;
    --ink: #2a2a2a;
    --rule: #4a4a4a;
    --paper: #ffffff;
    --backdrop: #e9eaee;
  }
  * { box-sizing: border-box; margin: 0; padding: 0; }
  html, body {
    width: 1200px; height: 880px; overflow: hidden;
    background: var(--backdrop);
    font-family: "Poppins", sans-serif;
  }
  .stage { position: relative; width: 1200px; height: 880px; }
  .card {
    position: absolute; left: 260px;
    width: 680px; height: 388px;
    border-radius: 26px;
    overflow: hidden;
    box-shadow: 0 10px 28px rgba(0,0,0,0.18);
  }
  /* Front */
  .card-front {
    top: 36px;
    background: var(--navy);
    color: var(--paper);
    display: flex; flex-direction: column; align-items: center; justify-content: center;
  }
  .wordmark {
    display: flex; align-items: center; gap: 16px;
    font-weight: 700; letter-spacing: -1px; line-height: 1;
  }
  .card-front .wordmark { font-size: 96px; color: var(--paper); }
  .wordmark .dot {
    width: 30px; height: 30px; border-radius: 50%; background: currentColor; flex: none;
  }
  .tagline {
    margin-top: 22px;
    font-size: 27px; font-weight: 700; letter-spacing: 0.3px;
  }
  /* Back */
  .card-back { top: 456px; background: var(--paper); color: var(--ink); }
  .card-back .wordmark {
    position: absolute; right: 56px; top: 48px;
    font-size: 64px; color: var(--brand-blue);
  }
  .card-back .wordmark .dot { width: 22px; height: 22px; }
  .accent-bar {
    position: absolute; left: 0; top: 232px;
    width: 14px; height: 50px; background: var(--brand-blue);
  }
  .person { position: absolute; left: 56px; top: 226px; }
  .person-name {
    font-size: 31px; font-weight: 700; color: var(--brand-blue); line-height: 1.1;
  }
  .person-role { font-size: 19px; font-weight: 400; color: var(--ink); margin-top: 4px; }
  .divider {
    position: absolute; left: 56px; right: 56px; top: 306px;
    height: 1.5px; background: var(--rule);
  }
  .contact {
    position: absolute; top: 322px;
    display: flex; align-items: center; gap: 10px;
    font-size: 19px; color: var(--ink);
  }
  .contact-phone { left: 56px; }
  .contact-email { right: 56px; }
  .contact svg { width: 20px; height: 20px; fill: var(--brand-blue); flex: none; }
</style>
</head>
<body>
<main class="stage">
  <section class="card card-front" aria-label="Card front">
    <div class="wordmark"><span class="dot"></span><span>Tarnwell</span></div>
    <p class="tagline">Your Poolside Official's Gateway</p>
  </section>

  <section class="card card-back" aria-label="Card back">
    <div class="wordmark"><span class="dot"></span><span>Tarnwell</span></div>
    <span class="accent-bar"></span>
    <div class="person">
      <h1 class="person-name">Dana Whitcombe</h1>
      <p class="person-role">CEO &amp; Founder</p>
    </div>
    <div class="divider"></div>
    <p class="contact contact-phone">
      <svg viewBox="0 0 24 24" aria-hidden="true"><path d="M6.6 10.8a15.2 15.2 0 0 0 6.6 6.6l2.2-2.2a1 1 0 0 1 1-.25 11.4 11.4 0 0 0 3.6.57 1 1 0 0 1 1 1V20a1 1 0 0 1-1 1A17 17 0 0 1 3 4a1 1 0 0 1 1-1h3.5a1 1 0 0 1 1 1c0 1.25.2 2.45.57 3.57a1 1 0 0 1-.25 1z"/></svg>
      <span>(555) 218-4470</span>
    </p>
    <p class="contact contact-email">
      <svg viewBox="0 0 24 24" aria-hidden="true"><path d="M2 5h20v14H2z M2 5l10 8 10-8" fill="none" stroke="#2f4a9e" stroke-width="2"/><path d="M2 5h20l-10 8z"/></svg>
      <span>dana@tarnwell.com</span>
    </p>
  </section>
</main>
</body>
</html>
```